Box design for toddler shoes

Hi,

TASK:
I need a shoe box designed for our rubber soled socks.

DIMENSION:
13.5cmHx12cmWx7.2cmD

​BOX FEATURE:
1. Must include the following information
a) our logo
b) the product name ‘Rubber Soled Socks’
c) Some product key features that could be written on the box include:
- Indoor and outdoor wear
- Soft and flexible sole
- Light weight and comfortable
d) Sock composition and care instructions also needs to be included on the box,
probably quite small. Maybe on the base.

Sock: 80% Cotton 10% Spandex 10% Polyester
Rubber Sole

Care instructions:
Cold Machine Wash or Hand Wash
Do not bleach
Do not tumble dry

Made in China
Distributed by TW Tots
www.twtots.com.au

2. A CUT OUT in the lid so you can see at least part of the shoe/sock pattern design. I am open to different size and shape cut outs, but need the shoes to not be at risk of falling out of the box.

DESIGN KEYPOINTS:
1. I would like a modern classic design. I like the yellow shoe box picture attached, but am happy and open for a different design. This just gives you the idea of the fresh look I like.

2. NO brown craft packaging, but am open to options for other colours.

3. NO picture of the socks on the box design
- the CUT on the lid will allow buyer to see the pattern on the socks. Attached is images of the sample shoe/socks that will be put in the boxes and how they will be packaged in the rectangle box. There are many different designs/colour. All will need to be packaged in the same box.

4. I'd love to see what the box would look like as it sits on the shelf, but also need the flat lay design ready for printing.

Please let me know if you have any questions to help with your design.

I can't wait to see your design.

Thanks,
Maya

Industry/Entity Type

Baby/kids

Font styles to use
Sans Serif
Other font styles liked:
• More modern version of Sans Serif

Requirements
Must have
• Cut out in the top of the box so you can see part of the sock to know which design is packaged inside.
Should not have
• Bubble font

```html
<!DOCTYPE html>
<html lang="en">
<head>
<meta charset="utf-8">
<title>Little Alden – Rubber Soled Socks Box Dieline</title>
<link rel="stylesheet" href="https://fonts.googleapis.com/css2?family=Oswald:wght@500;600&family=Questrial&family=Roboto:wght@400;700&display=swap">
<style>
  :root {
    --paper: #ffffff;
    --cut: #d81b5a;
    --fold: #29a8e0;
    --brand-red: #d50000;
    --brand-red-soft: #e8474a;
    --ink: #111111;
    --window: #c4c4c4;
  }
  html, body {
    margin: 0;
    padding: 0;
    width: 1200px;
    height: 886px;
    overflow: hidden;
    background: var(--paper);
  }
  .dieline {
    display: block;
    width: 1200px;
    height: 886px;
  }
  .spec-label { font-family: "Roboto", Arial, sans-serif; font-size: 18px; fill: var(--ink); }
  .spec-label .bold { font-weight: 700; }
  .cut-line { fill: none; stroke: var(--cut); stroke-width: 3; stroke-linejoin: miter; }
  .fold-line { fill: none; stroke: var(--fold); stroke-width: 1.6; stroke-dasharray: 4 3; }
  .deco-area { fill: url(#redWash); }
  .window-cut { fill: none; stroke: var(--window); stroke-width: 1.4; }
  .brand-name { font-family: "Questrial", sans-serif; fill: var(--ink); }
  .product-name { font-family: "Oswald", sans-serif; font-weight: 600; fill: var(--ink); }
  .feature-list { font-family: "Oswald", sans-serif; font-weight: 500; font-style: italic; font-size: 28px; fill: var(--ink); }
  .info-text { font-family: "Questrial", sans-serif; font-size: 13px; fill: var(--ink); }
  .info-heading { font-family: "Questrial", sans-serif; font-size: 12px; fill: #fff; }
  .info-heading-bg { fill: var(--ink); }
</style>
</head>
<body>
<svg class="dieline" viewBox="0 0 2040 1506" xmlns="http://www.w3.org/2000/svg">
  <defs>
    <linearGradient id="redWash" x1="0" y1="0" x2="1" y2="1">
      <stop offset="0" stop-color="var(--brand-red)"/>
      <stop offset="1" stop-color="var(--brand-red-soft)"/>
    </linearGradient>
  </defs>

  <text class="spec-label" x="2" y="16"><tspan class="bold">Card Box</tspan> 13.5×7.2×12 cm</text>

  <!-- decorative print areas -->
  <g class="artwork">
    <rect class="deco-area" x="640" y="460" width="345" height="355" role="img" aria-label="Red abstract wave decoration on the front panel"/>
    <rect class="deco-area" x="343" y="820" width="222" height="212" role="img" aria-label="Red abstract wave decoration in the front panel corner"/>
    <rect class="deco-area" x="985" y="462" width="341" height="353" role="img" aria-label="Red abstract wave decoration on the side panel"/>
    <rect class="deco-area" x="1742" y="1035" width="225" height="335" role="img" aria-label="Red abstract wave decoration on the base panel"/>
    <circle class="window-cut" cx="729" cy="625" r="127"/>
  </g>

  <!-- front panel -->
  <g class="front-panel">
    <text class="brand-name" x="473" y="684" font-size="44" text-anchor="middle">Little Alden</text>
    <text class="product-name" x="403" y="713" font-size="18" textLength="140" lengthAdjust="spacingAndGlyphs">Rubber Soled Socks</text>
    <g class="feature-list">
      <text x="612" y="937">• Indoor and outdoor wear</text>
      <text x="612" y="966">• Soft and flexible sole</text>
      <text x="612" y="995">• Light weight and comfortable</text>
    </g>
  </g>

  <!-- back panel -->
  <g class="back-panel">
    <text class="brand-name" x="1508" y="636" font-size="38" text-anchor="middle">Little Alden</text>
    <text class="product-name" x="1448" y="662" font-size="15" textLength="120" lengthAdjust="spacingAndGlyphs">Rubber Soled Socks</text>
    <g class="care-info">
      <rect class="info-heading-bg" x="1418" y="838" width="40" height="14"/>
      <text class="info-heading" x="1420" y="849">SOCK:</text>
      <text class="info-text" x="1419" y="865">80% Cotton 10% Spandex 10% Polyester Rubber Sole</text>
      <rect class="info-heading-bg" x="1418" y="870" width="131" height="14"/>
      <text class="info-heading" x="1420" y="881">CARE INSTRUCTIONS:</text>
      <text class="info-text" x="1419" y="897">Cold Machine Wash or Hand Wash</text>
      <text class="info-text" x="1419" y="913">Do not bleach</text>
      <text class="info-text" x="1419" y="929">Do not tumble dry</text>
      <text class="info-text" x="1419" y="961">Made in China</text>
      <text class="info-text" x="1419" y="977">Distributed by TW Tots</text>
      <text class="info-text" x="1419" y="993">www.twtots.com.au</text>
    </g>
  </g>

  <!-- base panel (inverted) -->
  <g class="base-panel" transform="rotate(180 1620 1195)">
    <text class="brand-name" x="1620" y="1215" font-size="58" text-anchor="middle">Little Alden</text>
    <text class="product-name" x="1514" y="1253" font-size="26" textLength="217" lengthAdjust="spacingAndGlyphs">Rubber Soled Socks</text>
  </g>

  <!-- fold lines -->
  <g class="folds">
    <path class="fold-line" d="M373,126 L955,126"/>
    <path class="fold-line" d="M5,462 L1326,462"/>
    <path class="fold-line" d="M3,1032 L1326,1032"/>
    <path class="fold-line" d="M343,462 L343,1032"/>
    <path class="fold-line" d="M985,462 L985,1032"/>
    <path class="fold-line" d="M1326,462 L1326,1035"/>
    <path class="fold-line" d="M1967,462 L1967,1035"/>
    <path class="fold-line" d="M1326,1035 L1967,1035"/>
    <path class="fold-line" d="M1352,1372 L1940,1372"/>
  </g>

  <!-- cut lines -->
  <g class="cuts">
    <path class="cut-line" d="M343,460 L343,121 L368,121 L373,126 M955,126 L960,121 L985,121 L985,460"/>
    <path class="cut-line" d="M346,121 L346,100 Q346,28 416,28 L912,28 Q982,28 982,100 L982,121"/>
    <path class="cut-line" d="M5,462 L5,440 L14,432 L64,244 L312,244 L329,446 L343,462"/>
    <path class="cut-line" d="M5,462 L3,462 L3,1032"/>
    <path class="cut-line" d="M3,1032 L16,1046 L34,1250 L281,1250 L331,1061 L342,1051 L342,1032 L987,1032"/>
    <path class="cut-line" d="M985,462 L998,448 L1016,244 L1264,244 L1316,436 L1325,446 L1325,462"/>
    <path class="cut-line" d="M987,1032 L987,1052 L997,1062 L1047,1250 L1294,1250 L1310,1046 L1326,1032"/>
    <path class="cut-line" d="M1325,462 L1625,462 L1628,466 A18,18 0 0 0 1664,466 L1668,462 L1967,462 L2038,475 L2038,1020 L1967,1032"/>
    <path class="cut-line" d="M1967,1032 L1967,1376 L1940,1376 L1945,1372"/>
    <path class="cut-line" d="M1326,1035 L1326,1376 L1352,1376 L1356,1372"/>
    <path class="cut-line" d="M1329,1376 L1329,1398 Q1329,1468 1399,1468 L1894,1468 Q1964,1468 1964,1398 L1964,1376"/>
  </g>
</svg>
</body>
</html>
```